BramliVex a new start up looking for packaging design for it's organic Cold pressed Peanut oil.

We require a labelling design for a new company based in the UK called ''BramliVex''. We will be launching Organic cold pressed peanut oil. We would like a design that is simple yet very catchy and not boring.

Target Market(s)
General consumers and healthy eaters, Vegan friendly

Colors
Designer to choose colors to be used in the design.

Must have
• Refer to Packaging document information for labelling.
• Type of bottle 250 ML Selvane bottle (refer to Bottle Picture doc.)
• Must have the "BramliVex" logo stamped somewhere on the front of the package (refer to the Logo document)
• Sleek and appetising design
• Neutral colors possible accents with logo colors
• Claims: Organic, Vegan, High in Monounsaturated fat, High in Poly-unsaturated fat(all this in front of the package)
• Made in the uk logo, and EU organic logo
• Social Media Icons (Pictaloom,Chatterdesk) as well as website (Bramlivex.co.uk)
• Space reserved at the back of the package for barcode and best before date to be printed on.
Be nice to have: picture of the product on the background if possible
Updates

Need extra days to review

Target Market(s)

Font styles to use
Serif
Sans Serif
Decorative
Script

Requirements
Must have

• • Refer to Packaging document information for labelling.

```html
<!DOCTYPE html>
<html lang="en">
<head>
<meta charset="utf-8">
<title>BramliVex Cold Pressed Peanut Oil – Label</title>
<link rel="stylesheet" href="https://fonts.googleapis.com/css2?family=Titan+One&family=Questrial&display=swap">
<style>
  :root {
    --page: #ffffff;
    --label: #c69c6d;
    --ink-dark: #4a1a0c;
    --ink-mid: #6b4630;
    --ink-claim: #7a3f22;
    --art-light: #d9b48a;
    --art-dark: #6a3420;
  }
  * { box-sizing: border-box; margin: 0; padding: 0; }
  html, body {
    width: 848px;
    height: 1200px;
    overflow: hidden;
    background: var(--page);
  }
  .canvas {
    position: relative;
    width: 848px;
    height: 1200px;
  }
  .label {
    position: absolute;
    left: 204px;
    top: 86px;
    width: 440px;
    height: 1029px;
    background: var(--label);
    border-radius: 220px 220px 14px 14px;
    color: var(--ink-dark);
  }
  .brand-name {
    position: absolute;
    top: 66px;
    left: 0;
    width: 100%;
    text-align: center;
    font-family: "Titan One", sans-serif;
    font-size: 46px;
    letter-spacing: 1px;
    color: var(--ink-dark);
  }
  .mascot-art {
    position: absolute;
    top: 136px;
    left: 160px;
    width: 120px;
    height: 190px;
    border-radius: 60px 60px 40px 40px;
    background: radial-gradient(circle at 50% 35%, var(--art-light) 0%, var(--art-dark) 70%);
  }
  .process {
    position: absolute;
    top: 402px;
    left: 0;
    width: 100%;
    text-align: center;
    font-family: "Questrial", sans-serif;
    font-size: 31px;
    letter-spacing: 5px;
    color: var(--ink-mid);
  }
  .product-name {
    position: absolute;
    top: 458px;
    left: 0;
    width: 100%;
    text-align: center;
    font-family: "Titan One", sans-serif;
    font-size: 52px;
    color: var(--ink-dark);
  }
  .claims {
    position: absolute;
    top: 696px;
    left: 26px;
    list-style: none;
    font-family: "Questrial", sans-serif;
    font-size: 22px;
    line-height: 29px;
    color: var(--ink-claim);
  }
  .claims li {
    display: flex;
    align-items: center;
    gap: 10px;
  }
  .claims svg {
    width: 12px;
    height: 14px;
    flex: none;
  }
  .volume {
    position: absolute;
    top: 928px;
    left: 0;
    width: 100%;
    text-align: center;
    font-family: "Questrial", sans-serif;
    font-size: 24px;
    font-weight: 700;
    color: var(--ink-dark);
  }
</style>
</head>
<body>
  <main class="canvas">
    <section class="label">
      <div class="brand-name">BramliVex</div>
      <div class="mascot-art" role="img" aria-label="Illustrated brand mascot eating a peanut"></div>
      <p class="process">COLD PRESSED</p>
      <h1 class="product-name">Peanut Oil</h1>
      <ul class="claims">
        <li><svg viewBox="0 0 12 14"><path d="M1 7 L4 12 L11 1" fill="none" stroke="currentColor" stroke-width="1.4"/></svg>Organic</li>
        <li><svg viewBox="0 0 12 14"><path d="M1 7 L4 12 L11 1" fill="none" stroke="currentColor" stroke-width="1.4"/></svg>Vegan</li>
        <li><svg viewBox="0 0 12 14"><path d="M1 7 L4 12 L11 1" fill="none" stroke="currentColor" stroke-width="1.4"/></svg>High in Monounsaturated fat</li>
        <li><svg viewBox="0 0 12 14"><path d="M1 7 L4 12 L11 1" fill="none" stroke="currentColor" stroke-width="1.4"/></svg>High in Poly-unsaturated fat</li>
      </ul>
      <p class="volume">250ml</p>
    </section>
  </main>
</body>
</html>
```